Awesome Podcast Artwork Needed :-)

I need an AWESOME piece of podcast artwork for a new podcast called "Keys To The Porch" :-)
The Podcast teaches "new" property investors... or people just starting out... the basics of property investing (real estate) by sharing tips, tricks, strategies, interviews etc.
I have a logo that I'm kind of happy with and have attached examples of it here labelled "Examples Of Logo". It basically consists of four houses hanging on some thread and although I'm certainly not saying you must use it. If you do want to use it, I would be open to you "modernising" it a bit - if needed - or rearranging the house images in a line (horizontally or vertically) or in a square... or indeed in anyway you feel works
In terms of design, I confess I'm really not sure what I want - only I certainly do want to give a sense my Podcast is about "Property Investing".
I have included 2 examples of artwork that my competition uses labelled "Competition Artwork 1&2". I have also included "My Attempt" at doing this... which I know isn't very good - because you can't clearly see the words and to be honest - it looks weak next to other podcast artwork (for example the "Beyond Brick Ledgers" artwork that I have included here). I have attached a mock up of a "Simulated Tunewell Screen" so you can see what I mean when I say my example looks weak compared to the others.
Lastly here's my new website (it's not yet out there) but that may give you some ideas of what I like: https://keystotheporch.example/home/
I'm excited to see what you come up with :-)
PS. The artwork needs to be 3000x3000 pixels with a DPI of 72
Target Market(s)
New property investors - people who want to learn how to invest in property (real estate)
Requirements
Must have
- The name "Keys To The Porch"
Nice to have
- If my logo... or a variation on my logo can be incorporated - that would be good - but not essential. I've attached examples but will happily consider modifications.
- Please do not feel however that you must include the logo.

```html
<!DOCTYPE html>
<html lang="en">
<head>
<meta charset="utf-8">
<title>Keys To The Porch – Podcast Artwork</title>
<link rel="stylesheet" href="https://fonts.googleapis.com/css2?family=Jost:wght@700;800&display=swap">
<style>
  :root {
    --orange-deep: #e8940c;
    --orange-mid: #f0a21e;
    --orange-light: #f6b94a;
    --stripe: rgba(255, 255, 255, 0.045);
    --white: #ffffff;
    --host-top: #b9c4cf;
    --host-mid: #2a3344;
    --host-low: #4f6f95;
  }
  html, body {
    margin: 0;
    padding: 0;
    width: 1200px;
    height: 1200px;
    overflow: hidden;
    background: var(--orange-mid);
  }
  .cover {
    position: relative;
    width: 1200px;
    height: 1200px;
    overflow: hidden;
    font-family: "Jost", "Futura", sans-serif;
    background:
      repeating-linear-gradient(135deg, var(--stripe) 0 6px, transparent 6px 14px),
      radial-gradient(circle at 85% 85%, var(--orange-light) 0%, var(--orange-mid) 45%, var(--orange-deep) 100%);
  }
  .brand-mark {
    position: absolute;
    left: 42px;
    top: 160px;
    display: flex;
    align-items: center;
    gap: 22px;
    color: var(--white);
    font-weight: 700;
    font-size: 60px;
    line-height: 1;
    letter-spacing: 1px;
  }
  .brand-mark__square {
    width: 48px;
    height: 48px;
    background: var(--white);
  }
  .show-title {
    position: absolute;
    left: 38px;
    top: 440px;
    margin: 0;
    color: var(--white);
    font-weight: 800;
    letter-spacing: 1px;
    text-transform: uppercase;
  }
  .show-title span {
    display: block;
    font-size: 222px;
    line-height: 0.86em;
    white-space: nowrap;
  }
  .show-title .show-title__last {
    font-size: 176px;
  }
  .host-photo {
    position: absolute;
    left: 690px;
    top: 74px;
    width: 510px;
    height: 1126px;
  }
</style>
</head>
<body>
  <main class="cover">
    <div class="brand-mark">
      <span class="brand-mark__square"></span>
      <span class="brand-mark__name">Keys To The Porch</span>
    </div>

    <h1 class="show-title">
      <span>Keys</span>
      <span>To</span>
      <span>The</span>
      <span class="show-title__last">Porch</span>
    </h1>

    <svg class="host-photo" viewBox="0 0 510 1126" role="img" aria-label="Photo of the smiling host standing in a navy blazer, light blue shirt and jeans, cut out with a white outline">
      <defs>
        <linearGradient id="host-tones" x1="0" y1="0" x2="0" y2="1">
          <stop offset="0" stop-color="var(--host-top)"/>
          <stop offset="0.2" stop-color="var(--host-mid)"/>
          <stop offset="0.6" stop-color="var(--host-mid)"/>
          <stop offset="1" stop-color="var(--host-low)"/>
        </linearGradient>
      </defs>
      <path d="M150 10 h150 q30 0 30 30 v170 q130 30 150 110 l20 540 h-70 v316 h-310 v-260 h-60 v-90 h-40 l10 -490 q20 -80 110 -110 v-186 q0 -30 30 -30 z"
            fill="url(#host-tones)" stroke="var(--white)" stroke-width="10" stroke-linejoin="round"/>
    </svg>
  </main>
</body>
</html>
```